Executive recruiting firm in need of business card design

Executive recruiting firm looking for a sleek, classy and modern business card design; card itself will be square shape, rounded edges and soft touch paper, our colors are dark blues in the navy color scale, silvers and grays. Reference our website for a better idea of our company's feel and goals at Staffvex.com - our company message is "Employee Engagement Begins at Recruitment" this should be on the card

Industry/Entity Type

Business

```html
<!DOCTYPE html>
<html lang="en">
<head>
<meta charset="utf-8">
<title>Staffvex Business Card</title>
<link rel="stylesheet" href="https://fonts.googleapis.com/css2?family=Poppins:wght@300;400;500;600&display=swap">
<style>
  :root {
    --navy: #1a1a4e;
    --navy-soft: #22225a;
    --white: #ffffff;
    --text-gray: #8a8a90;
    --stage: #3b3b3d;
  }
  * { margin: 0; padding: 0; box-sizing: border-box; }
  html, body {
    width: 1200px; height: 900px; overflow: hidden;
    background: var(--stage);
    font-family: "Poppins", sans-serif;
  }
  .stage {
    width: 1200px; height: 900px;
    display: flex; align-items: center; justify-content: center; gap: 40px;
  }
  .card {
    position: relative;
    width: 520px; height: 300px;
    border-radius: 22px;
    overflow: hidden;
    box-shadow: 0 10px 30px rgba(0,0,0,0.35);
  }
  /* Back side */
  .card-back { background: var(--navy); color: var(--white); }
  .back-decor {
    position: absolute; right: -40px; top: 40px;
    width: 300px; height: 300px; border-radius: 50%;
    background: var(--navy-soft);
  }
  .brand {
    position: absolute; left: 90px; top: 100px;
    display: flex; align-items: center; gap: 16px;
  }
  .brand-name {
    font-weight: 300; font-size: 40px; letter-spacing: 8px;
    color: var(--white);
  }
  .brand-dot {
    width: 70px; height: 70px; border-radius: 50%;
    background: var(--white);
  }
  .brand-sub {
    position: absolute; left: 92px; top: 152px;
    font-size: 9px; font-weight: 300; letter-spacing: 5px;
    color: var(--white);
  }
  .tagline {
    position: absolute; left: 0; right: 0; bottom: 52px;
    text-align: center;
    font-size: 13px; font-weight: 400; letter-spacing: 0.3px;
  }
  /* Front side */
  .card-front { background: var(--white); }
  .front-mark {
    position: absolute; left: 40px; top: 72px;
    width: 140px; display: flex; flex-direction: column; align-items: center; gap: 10px;
  }
  .front-circle {
    width: 130px; height: 130px; border-radius: 50%;
    background: var(--navy);
  }
  .front-name {
    font-size: 15px; font-weight: 400; letter-spacing: 4px;
    color: var(--navy);
  }
  .divider {
    position: absolute; left: 210px; top: 70px;
    width: 2px; height: 160px; background: var(--navy);
  }
  .details {
    position: absolute; left: 232px; top: 72px; right: 20px;
  }
  .person-name {
    font-size: 20px; font-weight: 600; color: var(--navy); line-height: 1.1;
  }
  .person-role {
    font-size: 13px; font-weight: 500; color: var(--text-gray); margin-bottom: 10px;
  }
  .address {
    font-size: 12px; font-weight: 400; color: var(--text-gray); line-height: 1.35;
    margin-bottom: 4px;
  }
  .contact-row {
    display: flex; align-items: center; gap: 8px;
    font-size: 12px; color: var(--text-gray); line-height: 1.6;
  }
  .contact-row svg { width: 12px; height: 12px; flex: none; fill: var(--navy); }
</style>
</head>
<body>
<main class="stage">
  <section class="card card-back" aria-label="Card back">
    <div class="back-decor"></div>
    <div class="brand">
      <span class="brand-name">STAFFVEX</span>
      <span class="brand-dot"></span>
    </div>
    <span class="brand-sub">talent acquisition</span>
    <p class="tagline">Employee Engagement Begins at Recruitment</p>
  </section>

  <section class="card card-front" aria-label="Card front">
    <div class="front-mark">
      <span class="front-circle"></span>
      <span class="front-name">STAFFVEX</span>
    </div>
    <div class="divider"></div>
    <div class="details">
      <p class="person-name">Maren Alder</p>
      <p class="person-role">Founder</p>
      <p class="address">118 Harbor Lane Suite #<br>410 Brookfield NY 10099</p>
      <p class="contact-row">
        <svg viewBox="0 0 24 24" aria-hidden="true"><path d="M6.6 10.8a15.1 15.1 0 0 0 6.6 6.6l2.2-2.2a1 1 0 0 1 1-.25 11.4 11.4 0 0 0 3.6.6 1 1 0 0 1 1 1V20a1 1 0 0 1-1 1A17 17 0 0 1 3 4a1 1 0 0 1 1-1h3.5a1 1 0 0 1 1 1c0 1.25.2 2.45.6 3.6a1 1 0 0 1-.25 1z"/></svg>
        +1.555.204.3817
      </p>
      <p class="contact-row">
        <svg viewBox="0 0 24 24" aria-hidden="true"><path d="M7 1h10a2 2 0 0 1 2 2v18a2 2 0 0 1-2 2H7a2 2 0 0 1-2-2V3a2 2 0 0 1 2-2zm0 3v15h10V4z"/></svg>
        555-381-0942
      </p>
      <p class="contact-row">
        <svg viewBox="0 0 24 24" aria-hidden="true"><path d="M2 5h20v14H2zm2 2v.5l8 5 8-5V7zm0 3v7h16v-7l-8 5z"/></svg>
        malder@staffvex.com
      </p>
    </div>
  </section>
</main>
</body>
</html>
```